Marketing Flyer

We are looking for a flyer that will clearly and simply explain that we are an internet, tv, and telephone provider for the business community. we compete with major providers. we offer a triple play package as well tv internet and phone

Target Market(s)

small to medium sixed business

Industry/Entity Type

Telecom

Font styles to use
Serif

Colors

Designer to choose colors to be used in the design.

Requirements
Must have
• logo, hip, current industry buzz words fun life
Nice to have
• color,
Should not have
• must not be dull and over simple

```html
<!DOCTYPE html>
<html lang="en">
<head>
<meta charset="utf-8">
<title>Brightwave Business – Tech Solutions Flyer</title>
<link rel="stylesheet" href="https://fonts.googleapis.com/css2?family=Oswald:wght@500;700&family=Lato:wght@400;700&display=swap">
<style>
  :root {
    --page-bg: #e9e9e9;
    --navy-deep: #1a3152;
    --navy: #244a78;
    --blue-glow: #4a8cc4;
    --orange: #d9461b;
    --orange-dark: #a8300e;
    --orange-light: #ec5a26;
    --white: #ffffff;
    --text-soft: #e6edf5;
  }
  * { box-sizing: border-box; margin: 0; padding: 0; }
  html, body {
    width: 1200px; height: 1024px; overflow: hidden;
    background: var(--page-bg);
  }
  .flyer {
    position: absolute; left: 243px; top: 12px;
    width: 714px; height: 1000px; overflow: hidden;
    background: radial-gradient(ellipse 70% 55% at 50% 45%, var(--blue-glow) 0%, var(--navy) 55%, var(--navy-deep) 100%);
    box-shadow: 0 4px 14px rgba(0,0,0,.3);
    font-family: "Lato", sans-serif;
    color: var(--white);
  }
  .headline {
    position: absolute; top: 58px; left: 0; width: 100%;
    text-align: center; font-family: "Oswald", sans-serif; font-weight: 700;
    text-transform: uppercase; line-height: 1;
    text-shadow: 0 2px 4px rgba(0,0,0,.35);
  }
  .headline .line-top { display: block; font-size: 43px; letter-spacing: .3px; }
  .headline .line-main { display: block; font-size: 72px; margin-top: 4px; }

  .monitor-photo {
    position: absolute; left: 179px; top: 220px; width: 428px; height: 275px;
    background: linear-gradient(150deg, #dbe8f3 0%, #a9c6df 45%, #6f92b4 100%);
    border: 5px solid #15181d;
  }
  .laptop-screen {
    position: absolute; left: 110px; top: 369px; width: 236px; height: 155px;
    background: var(--white); border: 6px solid #15181d; border-radius: 4px 4px 0 0;
    display: flex; align-items: center; justify-content: center; gap: 8px;
  }
  .laptop-base {
    position: absolute; left: 96px; top: 524px; width: 296px; height: 6px;
    background: linear-gradient(180deg, #d7d9dc, #8c9095); border-radius: 0 0 6px 6px;
  }
  .brand-mark { width: 12px; height: 12px; background: var(--navy-deep); }
  .brand-name {
    font-family: "Lato", sans-serif; font-weight: 700; font-size: 20px;
    color: var(--navy-deep);
  }
  .phone-photo {
    position: absolute; left: 442px; top: 432px; width: 86px; height: 120px;
    background: linear-gradient(180deg, #3b3e43, #16181b); border-radius: 10px;
  }

  .features { position: absolute; top: 606px; left: 63px; display: flex; gap: 39px; }
  .feature {
    width: 171px; height: 131px; border-radius: 12px;
    background: linear-gradient(180deg, var(--orange-dark) 0%, var(--orange) 55%, var(--orange-light) 100%);
    box-shadow: 0 3px 10px rgba(0,0,0,.35);
    display: flex; flex-direction: column; align-items: center; justify-content: center;
    text-align: center; font-family: "Oswald", sans-serif; font-weight: 500;
    padding: 6px 8px;
  }
  .feature svg { width: 44px; height: 36px; margin-bottom: 4px; }
  .feature .lead { font-size: 14px; line-height: 1.25; }
  .feature .big { font-size: 30px; font-weight: 700; line-height: 1; }
  .feature .big.stack { font-size: 25px; line-height: .95; }

  .about { position: absolute; left: 29px; top: 786px; width: 442px; }
  .about h2 {
    font-family: "Oswald", sans-serif; font-weight: 500; font-size: 14px;
    margin-bottom: 8px;
  }
  .about p { font-size: 10px; line-height: 1.27; color: var(--text-soft); margin-bottom: 11px; }

  .package-ribbon { position: absolute; left: 492px; top: 790px; width: 200px; height: 200px; }
  .package-ribbon .label {
    position: absolute; left: 18px; top: 42px; width: 170px;
    transform: rotate(-18deg); text-align: center;
    font-family: "Oswald", sans-serif; font-weight: 700; color: var(--white);
    line-height: .95;
  }
  .package-ribbon .label .title { display: block; font-size: 28px; text-transform: uppercase; }
  .package-ribbon .label .sub { display: block; font-family: "Lato", sans-serif; font-weight: 400; font-size: 12px; margin-top: 3px; }

  .contact-bar {
    position: absolute; left: 0; bottom: 0; width: 100%; height: 56px;
    background: var(--orange);
    display: flex; align-items: center; gap: 34px; padding-left: 34px;
    font-family: "Oswald", sans-serif; font-weight: 500; font-size: 14.5px;
  }
  .contact-bar .item { display: flex; align-items: center; gap: 12px; }
  .contact-bar svg { width: 13px; height: 13px; }
</style>
</head>
<body>
  <main class="flyer">
    <h1 class="headline">
      <span class="line-top">Tech Solutions of Tomorrow</span>
      <span class="line-main">For Today</span>
    </h1>

    <div class="monitor-photo" role="img" aria-label="Photo on a monitor: hands using a tablet showing colourful charts"></div>
    <div class="laptop-screen">
      <span class="brand-mark"></span>
      <span class="brand-name">Brightwave Business</span>
    </div>
    <div class="laptop-base"></div>
    <div class="phone-photo" role="img" aria-label="Photo of a black cordless desk phone on its base"></div>

    <section class="features">
      <div class="feature">
        <svg viewBox="0 0 44 36" fill="none" stroke="#fff" stroke-width="2">
          <path d="M12 26h22a7 7 0 0 0 0-14 10 10 0 0 0-19-2 8 8 0 0 0-3 16z"/>
          <path d="M20 26v6M26 26v4"/>
        </svg>
        <span class="lead">We are our own Voice<br>Over IP Provider</span>
        <span class="big">(VoIP)</span>
      </div>
      <div class="feature">
        <svg viewBox="0 0 44 36" fill="none" stroke="#fff" stroke-width="2">
          <rect x="15" y="16" width="14" height="12" rx="2"/>
          <path d="M18 16v-4a4 4 0 0 1 8 0v4"/>
          <circle cx="22" cy="22" r="1.5" fill="#fff"/>
        </svg>
        <span class="lead">The latest innovations in</span>
        <span class="big stack">Cyber<br>Security</span>
      </div>
      <div class="feature">
        <svg viewBox="0 0 44 36" fill="none" stroke="#fff" stroke-width="2">
          <path d="M11 27h22a7 7 0 0 0 0-14 10 10 0 0 0-19-2 8 8 0 0 0-3 16z"/>
          <circle cx="22" cy="21" r="4"/>
          <path d="M22 14v2M22 26v2M15 21h2M27 21h2"/>
        </svg>
        <span class="lead">Management, Monitoring,<br>and Support</span>
        <span class="big">24 / 7 / 365</span>
      </div>
    </section>

    <section class="about">
      <h2>INDUSTRY BEST STAFF !</h2>
      <p>Our team consists of a group of men and women with extensive experience in IT and Managed Services. We are comprised of Administrators, Managers, Engineers, Technicians, Marketers &amp; Sales Professionals so that we can deliver world class full scope service to your businesses, when and where you need it.</p>
      <p>IT Solutions are fluid in nature and are constantly evolving. We pride ourselves on continually adapting in order to bring our client's more than they have come to expect from other technology providers. We set the bar for customer service and are known for being the first to offer the latest and greatest. Our goals can only be met through choosing the best platforms available today.</p>
    </section>

    <div class="package-ribbon">
      <svg viewBox="0 0 200 200" width="200" height="200">
        <polygon points="0,55 192,0 172,108 140,123 160,160 120,200 100,120 24,135" fill="#c23a12"/>
        <polygon points="0,55 192,0 172,108 24,135" fill="var(--orange)"/>
        <polygon points="100,120 140,123 120,200" fill="var(--navy-deep)"/>
      </svg>
      <div class="label">
        <span class="title">Triple Play<br>Package</span>
        <span class="sub">TV, Internet &amp; Phone</span>
      </div>
    </div>

    <footer class="contact-bar">
      <span class="item">
        <svg viewBox="0 0 14 14" fill="var(--navy-deep)"><path d="M1 4c0-2 2-3 6-3s6 1 6 3l-3 1-1-2H5L4 5zM3 6h8l2 7H1z"/></svg>
        555-014-2290
      </span>
      <span class="item">
        <svg viewBox="0 0 14 14" fill="var(--navy-deep)"><rect x="1" y="3" width="12" height="9" rx="1"/><path d="M1 3l6 5 6-5" stroke="#d9461b" fill="none"/></svg>
        hello@brightwave.example
      </span>
      <span class="item">
        <svg viewBox="0 0 14 14" fill="none" stroke="var(--navy-deep)" stroke-width="1.5"><circle cx="7" cy="7" r="6"/><path d="M1 7h12M7 1c3 3 3 9 0 12M7 1c-3 3-3 9 0 12"/></svg>
        hello@brightwave.example
      </span>
    </footer>
  </main>
</body>
</html>
```